Sell the dream! Property investment proposal document

We are looking for a proposal document which outlines our vision for property development. The purpose of the document is to raise investment from investors - sell the dream!
Brief summary:
Tarrow Dwellings Developments, is an emerging New Zealand property investment company with a focus on providing unique property investment opportunities.
Our expertise and capabilities in architectural modular homes provide us with a remarkable advantage in tackling the development of properties that are typically considered challenging, remote, or uniquely positioned.
Our specialization in this niche sector of property development not only sets us apart from competitors, but also paves the way for lucrative investment opportunities in the New Zealand property market.
Feel free to use any images from www.tarrowdwellings.co.nz
Target Market(s)
investors for a unique property development opportunity
Industry/Entity Type
luxury property development in unique locations throughout New Zealand
Font styles to use
Colors
Designer to choose only greyscale colors for use in the design.
Look and feel

```html
<!DOCTYPE html>
<html lang="en">
<head>
<meta charset="utf-8">
<title>Tarrow Dwellings Developments – Investment Proposal</title>
<link href="https://fonts.googleapis.com/css2?family=Roboto:wght@400;500;700&display=swap" rel="stylesheet">
<style>
:root{
  --backdrop:#dcdedd;
  --page:#333333;
  --ink:#ffffff;
  --ink-soft:#e4e4e4;
  --rule:#8c8c8c;
  --spine:#4a4a4a;
}
*{margin:0;padding:0;box-sizing:border-box}
html,body{width:1200px;height:2162px;overflow:hidden;background:var(--backdrop)}
body{position:relative;font-family:'Roboto',Arial,sans-serif;color:var(--ink)}
.spread{position:absolute;left:212px;width:776px;height:549px;background:var(--page);overflow:hidden}
.spread::after{content:"";position:absolute;left:388px;top:0;width:1px;height:100%;background:var(--spine)}
.photo{position:absolute}
.abs{position:absolute}
.heading{font-size:11px;font-weight:500;letter-spacing:.1px}
.sub{font-size:8.5px;font-weight:500}
.body{font-size:7px;line-height:9.2px;color:var(--ink-soft)}
.lead{font-weight:700;color:var(--ink)}
.benefit-list{position:absolute;width:213px}
.benefit{position:relative;border-top:1px solid var(--rule);padding:3px 0 3px 27px}
.benefit:last-child{border-bottom:1px solid var(--rule)}
.benefit .num{position:absolute;left:0;top:50%;transform:translateY(-50%);width:19px;height:19px;border:1px solid var(--ink);border-radius:50%;font-size:6.5px;display:flex;align-items:center;justify-content:center}
.benefit h4{font-size:7px;font-weight:700;line-height:8.5px}
.benefit p{font-size:7px;line-height:9.2px;color:var(--ink-soft)}
.advantages{position:absolute;left:36px;top:64px;width:213px;list-style:none}
.advantages li{height:43px;border-top:1px solid var(--rule);display:flex;align-items:center;font-size:8.2px}
.advantages li:last-child{border-bottom:1px solid var(--rule)}
.advantages li::before{content:"";width:4.5px;height:4.5px;border-radius:50%;background:var(--ink);margin-right:5px}
.specs{position:absolute;left:36px;top:343px;width:139px;border-collapse:collapse;font-size:7px;line-height:9.2px}
.specs td{vertical-align:top;padding:2px 0;color:var(--ink-soft)}
.specs tr{border-top:1px solid var(--rule)}
.specs tr:last-child{border-bottom:1px solid var(--rule)}
.specs td:first-child{width:47px}
.bullets{list-style:none;font-size:7px;line-height:9.3px;color:var(--ink-soft)}
.bullets li{position:relative;padding-left:12px}
.bullets li::before{content:"";position:absolute;left:2px;top:3px;width:4px;height:4px;border-radius:50%;background:var(--ink)}
</style>
</head>
<body>

<!-- Spread one: benefits -->
<section class="spread" style="top:128px">
  <h2 class="heading abs" style="left:36px;top:36px">Benefits of building offsite</h2>
  <p class="body abs" style="left:36px;top:64px;width:213px">From higher quality control and efficient project management through to cost efficiencies and beyond: offsite is the stress-free way to build.</p>
  <div class="benefit-list" style="left:36px;top:108px">
    <div class="benefit"><span class="num">1</span><h4>Controlled costs</h4><p>Our ability to use standardised building methods within a purpose built, covered facility means less cost fluctuation due to unforeseen circumstances.</p></div>
    <div class="benefit"><span class="num">2</span><h4>Controlled timeframes</h4><p>Planning ahead, bulk purchasing of materials and not being delayed by weather conditions or site-specific issues (noise to neighbours or accessibility) means we can get on with the job at hand and deliver within controlled timeframes.</p></div>
    <div class="benefit"><span class="num">3</span><h4>Controlled quality</h4><p>Building in one single facility means we can call on all our building experts at any point of the process. Building indoors also means no weather disruption and a dry building during the framing stage.</p></div>
    <div class="benefit"><span class="num">4</span><h4>Fast turnaround times</h4><p>Our manufacturing processes have been tried, perfected and are independent of weather or site constraints which allows for a regimented building phase and fast turnaround times.</p></div>
    <div class="benefit"><span class="num">5</span><h4>Accessibility</h4><p>Instead of taking all our tools and materials to site, we take the finished parts of the building ready for assembly. This means: less transportation requirements, easier to access the site, and cost efficiencies for all involved.</p></div>
    <div class="benefit"><span class="num">6</span><h4>Stress free</h4><p>You make all the fun decisions, we do all the hard work. Our centralised building factory and range of specialists means we can offer full construction project management.</p></div>
    <div class="benefit"><span class="num">7</span><h4>Zero construction moisture rating</h4><p>Building indoors — especially during the framing stage — ensures those critical, internal components will remain moisture free for a healthy, durable home.</p></div>
  </div>
  <div class="photo" role="img" aria-label="Interior corner with tall glazing looking out to the sea, a concrete column and a low timber table" style="left:286px;top:0;width:203px;height:549px;background:linear-gradient(180deg,#8d8a86 0%,#c9cdd0 30%,#b4b7b8 55%,#8e8074 72%,#5c4a3a 88%,#3a3633 100%)"></div>
  <div class="benefit-list" style="left:526px;top:108px">
    <div class="benefit"><span class="num">8</span><h4>Ability to plan ahead and store materials</h4><p>We pre-book our builds well ahead of delivery times. This allows us to order materials well in advance and helps mitigate delivery delays and supply chain issues.</p></div>
    <div class="benefit"><span class="num">9</span><h4>Minimal property disturbance</h4><p>By delivering prefabricated and ready-to-assemble components to your site we minimise the number of workers, tools, vehicles and time required on site. Your property (and neighbours!) will thank you.</p></div>
  </div>
  <div class="photo" role="img" aria-label="Dark timber-clad modular cabin with glazed corner on a green lawn" style="left:526px;top:240px;width:250px;height:309px;background:linear-gradient(180deg,#b8c0c4 0%,#7b8178 25%,#2e2b28 45%,#3d3a33 62%,#5d7336 72%,#4d6a2b 100%)"></div>
</section>

<!-- Spread two: key advantages -->
<section class="spread" style="top:806px">
  <h2 class="heading abs" style="left:36px;top:36px">The key advantages</h2>
  <ul class="advantages">
    <li>High returns on investment 10-20%</li>
    <li>Fast turn arounds on investment (9-11 months)</li>
    <li>Controlled timelines</li>
    <li>Controlled costs</li>
    <li>Be a part of an exciting journey</li>
  </ul>
  <div class="photo" role="img" aria-label="Single-level dark home wrapped around a courtyard terrace under trees and blue sky" style="left:286px;top:0;width:490px;height:279px;background:linear-gradient(180deg,#c7d6e3 0%,#dfe4e6 30%,#6f7a5a 52%,#2f2d2b 64%,#8a857c 74%,#6c8a3c 84%,#5d7a31 100%)"></div>
  <div class="photo" role="img" aria-label="Two-storey dark home with garage above a landscaped driveway" style="left:0;top:316px;width:388px;height:195px;background:linear-gradient(180deg,#9aa2a4 0%,#c8ccca 25%,#2d2d2c 50%,#3e4a32 72%,#b9bab6 88%,#a9aaa6 100%)"></div>
  <div class="photo" role="img" aria-label="Stacked dark modular home among trees and hills with a paved path" style="left:388px;top:316px;width:351px;height:195px;background:linear-gradient(180deg,#c5ccd0 0%,#6d7b5e 30%,#262625 52%,#3f5530 74%,#cfd0cc 90%,#b5b6b2 100%)"></div>
</section>

<!-- Spread three: the designer series -->
<section class="spread" style="top:1483px">
  <div class="photo" role="img" aria-label="Long glazed pavilion home at dusk with lit pool terrace" style="left:0;top:37px;width:388px;height:159px;background:linear-gradient(180deg,#9aa6ae 0%,#d9d3c5 35%,#2b2a29 55%,#6b6760 70%,#56703a 85%,#4a6331 100%)"></div>
  <h2 class="heading abs" style="left:36px;top:230px">The Designer Series No. 1</h2>
  <p class="abs" style="left:36px;top:257px;width:140px;font-size:7px;line-height:9.2px;font-weight:700">A sophisticated, glazed pavilion with open plan, social spaces at its heart. A modernist and timeless design that maximises views, natural light and presence.</p>
  <h3 class="sub abs" style="left:36px;top:322px">Specifications</h3>
  <table class="specs">
    <tr><td>Rooms</td><td>3 Bedrooms<br>2.0 Bathrooms<br>Open Plan Living Room<br>Dining Room<br>Laundry</td></tr>
    <tr><td>Size</td><td>130.3 sqm</td></tr>
    <tr><td>Dimensions</td><td>34.6m long x 4.2–5m wide</td></tr>
    <tr><td>Price range</td><td>$778,000 - $900,000<br>Inc. GST (Excluding site specific costs)</td></tr>
  </table>
  <div class="photo" role="img" aria-label="Dark bedroom with grey bed, rug and floor-to-ceiling window" style="left:212px;top:233px;width:176px;height:227px;background:linear-gradient(90deg,#c9cfcf 0%,#8e948c 18%,#2c2b2a 40%,#4a4846 70%,#3a3938 100%)"></div>
  <p class="abs" style="left:36px;top:481px;width:316px;font-size:7px;line-height:9.2px;font-weight:700">Customisation is at the heart of what we do here at Tarrow so that your home can best take advantage of its site and reflect you and your family’s lifestyle. If you can imagine it, we can make it happen.</p>

  <h3 class="sub abs" style="left:424px;top:37px">Inclusions</h3>
  <p class="body abs" style="left:424px;top:62px;width:140px">Tarrows come with high-quality designer fittings, surfaces and finishes as part of our standard offering. Preference is given to New Zealand products — when possible — and to brands with a proven track record of quality and longevity.</p>
  <ul class="bullets abs" style="left:424px;top:128px;width:145px">
    <li>Ardene Ember shiplap cladding</li>
    <li>Internal gutter with a parapet</li>
    <li>Engineered oak flooring</li>
    <li>Holloway Marsh carpet</li>
    <li>Designer acrylic kitchen &amp; kitchen island with Veldastone benchtops</li>
    <li>Fully tiled bathrooms with large format slab tiles</li>
    <li>Tiled walk in showers with recessed shower shelves and LED lighting</li>
    <li>Full height internal doors</li>
    <li>Expansive joinery with engineered steel portals</li>
    <li>Full height joinery throughout</li>
    <li>Glass louvers on each slider</li>
  </ul>
  <h3 class="sub abs" style="left:600px;top:37px">Add-ons</h3>
  <p class="body abs" style="left:600px;top:62px;width:143px">Upgrades in a variety of architectural and interior details, material and colour palettes, amenities and additional rooms are available for that touch of luxury or added comfort. Many more upgrades are also available upon request.</p>
  <ul class="bullets abs" style="left:600px;top:128px;width:145px">
    <li>Garage</li>
    <li>Shiplap cedar cladding</li>
    <li>Kestrel cladding</li>
    <li>Concrete slab foundation with a polished finish</li>
    <li>Concrete-look flooring</li>
    <li>Slatwell systems</li>
    <li>Underfloor heating</li>
    <li>Increased internal stud height</li>
    <li>Feature walls</li>
    <li>Fireplace</li>
    <li>Solar power</li>
  </ul>
  <div class="photo" role="img" aria-label="Long dining room with dark table and chairs beside full-height glazing and sheer curtains" style="left:388px;top:300px;width:388px;height:212px;background:linear-gradient(90deg,#d4d6d2 0%,#9fa39a 18%,#5a5752 40%,#3b3835 55%,#b8ada0 78%,#e2dcd3 100%)"></div>
</section>

</body>
</html>
```